Real Estate Agent Announcement

I need an announcement postcard designed with imagery almost exactly similar to below; one side imagery and copy on the other. Palette is either desired in neutrals: off white, warm white, or very soft grey. I'd like to stick as close to example below in feeling of image evoking opulence and text to be clean and elegant. need double sided card with simple logo on the back. copy of logo attached. editable file type.

Target Market(s)

Luxury real estate market northern california

Industry/Entity Type

Real Estate

Font styles to use
Serif

```html
<!DOCTYPE html>
<html lang="en">
<head>
<meta charset="utf-8">
<title>Announcement Postcard – Light and Dark Versions</title>
<link href="https://fonts.googleapis.com/css2?family=Gafata&display=swap" rel="stylesheet">
<style>
  :root {
    --backdrop: #e8e5e0;
    --card-edge: #ffffff;
    --panel-light-top: #ffffff;
    --panel-light-bottom: #f1f1f1;
    --panel-dark: #000000;
    --ink-grey: #6a6a6a;
    --ink-soft: #7a7a7a;
    --ink-light: #e6e6e6;
    --accent-amber: #d9822b;
    --photo-cream: #e9dfcc;
    --photo-warm: #b99a70;
    --photo-deep: #6b4a32;
  }
  * { margin: 0; padding: 0; box-sizing: border-box; }
  html, body {
    width: 1200px; height: 1200px; overflow: hidden;
    background: var(--backdrop);
    font-family: "Gafata", "Trebuchet MS", sans-serif;
  }
  .postcard {
    position: absolute; left: 24px; width: 814px; height: 584px;
    background: var(--card-edge);
    box-shadow: 0 2px 6px rgba(0,0,0,0.25);
  }
  .postcard--light { top: 14px; }
  .postcard--dark { top: 606px; }
  .postcard__photo {
    position: absolute; left: 14px; top: 14px; width: 393px; height: 556px;
    background:
      linear-gradient(180deg, rgba(255,255,255,0.15) 0%, rgba(0,0,0,0) 40%, rgba(60,35,20,0.35) 100%),
      linear-gradient(90deg, var(--photo-cream) 0%, var(--photo-warm) 45%, var(--photo-deep) 75%, var(--photo-warm) 100%);
  }
  .postcard__panel {
    position: absolute; left: 407px; top: 14px; width: 393px; height: 556px;
    text-align: center;
  }
  .postcard--light .postcard__panel {
    background: radial-gradient(ellipse at 50% 35%, var(--panel-light-top) 0%, var(--panel-light-bottom) 100%);
  }
  .postcard--dark .postcard__panel { background: var(--panel-dark); }
  .agent-name {
    position: absolute; top: 132px; width: 100%;
    font-size: 34px; font-weight: 400; letter-spacing: 0.5px;
    color: var(--ink-grey);
  }
  .announcement {
    position: absolute; top: 194px; width: 100%;
    font-size: 18px; line-height: 23px; color: var(--ink-soft);
  }
  .values {
    position: absolute; top: 312px; width: 100%;
    font-size: 18px; line-height: 23px; color: var(--ink-soft);
  }
  .values__pillars { text-transform: uppercase; }
  .brand {
    position: absolute; top: 428px; width: 100%;
    display: flex; flex-direction: column; align-items: center;
  }
  .brand__name {
    display: flex; align-items: center; gap: 6px;
    font-size: 14px; line-height: 16px; color: var(--ink-grey);
  }
  .brand__dot { width: 9px; height: 9px; border-radius: 50%; background: var(--ink-grey); }
  .brand__tagline {
    margin-top: 6px; font-size: 8px; color: var(--ink-soft); letter-spacing: 0.3px;
  }
  .office-address {
    position: absolute; top: 506px; width: 100%;
    font-size: 12px; line-height: 16px; color: var(--ink-soft);
  }
  .postcard--dark .agent-name,
  .postcard--dark .values__pillars { color: var(--accent-amber); }
  .postcard--dark .announcement,
  .postcard--dark .values__line,
  .postcard--dark .office-address,
  .postcard--dark .brand__name,
  .postcard--dark .brand__tagline { color: var(--ink-light); }
  .postcard--dark .brand__dot { background: var(--ink-light); }
</style>
</head>
<body>

<section class="postcard postcard--light">
  <div class="postcard__photo" role="img" aria-label="Photograph of an opulent bedroom with canopy bed, fireplace, tufted armchair and ottoman"></div>
  <div class="postcard__panel">
    <h1 class="agent-name">CLARA VENSLEY</h1>
    <p class="announcement">is pleased to announce<br>her affiliation with<br>Harrow Lane Realty.</p>
    <p class="values"><span class="values__pillars">Integrity | Knowledge</span><br><span class="values__line">all of your needs.</span></p>
    <div class="brand">
      <div class="brand__name"><span class="brand__dot"></span>The Mara Quill Network</div>
      <div class="brand__tagline">care • commitment • creativity</div>
    </div>
    <p class="office-address">418 Alder Crest Way Ste. 300<br>Oakmont, CA 94610</p>
  </div>
</section>

<section class="postcard postcard--dark">
  <div class="postcard__photo" role="img" aria-label="Photograph of an opulent bedroom with canopy bed, fireplace, tufted armchair and ottoman"></div>
  <div class="postcard__panel">
    <h1 class="agent-name">CLARA VENSLEY</h1>
    <p class="announcement">is pleased to announce<br>her affiliation with<br>Harrow Lane Realty.</p>
    <p class="values"><span class="values__pillars">Integrity | Knowledge</span><br><span class="values__line">all of your needs.</span></p>
    <div class="brand">
      <div class="brand__name"><span class="brand__dot"></span>The Mara Quill Network</div>
      <div class="brand__tagline">care • commitment • creativity</div>
    </div>
    <p class="office-address">418 Alder Crest Way Ste. 300<br>Oakmont, CA 94610</p>
  </div>
</section>

</body>
</html>
```